VORELA.GYM Health & Fitness Online - Around me page

I need the design of an "around me" page for a mobile app. This page when opening should display a map, with identified points on the map and a list of the items seen on the map. All the subscreens also need to be designed and should include the following.
The "Around me" page is a mobile app screen that displays
- Health and fitness facilities around me on a map and on a list, these can include:
- Fitness Centers, Hotels that have Gyms, Fitness Studios, Wellness & SPA, Group fitness classes
The user also has the possibility to add a new location
The user has the possibility to search in general or use filters on the search, these filters include
- What are you looking for?
- Fitness Facility
- Functional area, free weights, cardio machines, workout machines
- Wellness
- Swimming pool, Sauna, Hamam, Massage
- Group classes
- Search by fitness program, fitness type, fitness Brand
- Professional
- Personal trainer, nutritionist, Physiotherapist, Fitness Instructor, Coach
When the user selects one item on the map, the selected entry on the list gets selected, depending on the item type some info is shown, by selecting the item on the list a detail page is displayed, with all the information of the item.
For example, if it's a fitness, it should show a profile picture, a logo, the address, contact information, the opening hours, the possibility to buy the access to the fitness. The size of the fitness, the capabilities of the fitness (free weight, cardio, sauna etc etc)
If it's a hotel, the same type of info like for the gym should display, just it needs to be clear it is a hotel with a fitness, what's important are the facilities and it's contents. Again The user can book this facility.
Upon booking the facility the user gets to see a QR code, this QR code will be scanned at the entrance.
If the item is a group fitness class, it can be delivered at a gym or studio, capacity info is required, the instructor that is presenting the class, the day and time of the class, and a button to book the class.
The item can also be a professional, in this case, his profile picture is shown, with his name and country, the languages he speaks, the programs he's certified on, his bio and experience, where he works, and the services he delivers, there is also a book this professional button, where the user can send a message to the professional.
Please make these screens modern, functional, simple, UX easy and intuitive experience for the user.
Please use the color-coding of the template I will send you, this template is not well designed, so please propose something 1000x better.
Target Market(s)
Users of this page are prople that are looking for a place to do fitness.
Industry/Entity Type
Health and Fitness
- I use Sketch for my design, if you can make it or in a format where I can import it to sketch it would help.

```html
<!DOCTYPE html>
<html lang="en">
<head>
<meta charset="utf-8">
<title>VORELA.GYM – Around Me</title>
<link href="https://fonts.googleapis.com/css2?family=Roboto:wght@400;500;700;900&display=swap" rel="stylesheet">
<style>
:root{
  --pink:#e23e62;
  --coral:#f86b5a;
  --orange:#f9a857;
  --dark:#2b2f3c;
  --map:#2c2d31;
  --map-light:#3d3e42;
  --map-road:#6b5a2a;
  --paper:#f7f7f8;
  --white:#ffffff;
  --muted:#9aa0ad;
  --star:#f5b82e;
  --row:#eef0f4;
}
*{box-sizing:border-box;margin:0;padding:0}
html,body{width:1200px;height:857px;overflow:hidden}
body{font-family:"Roboto",sans-serif;background:var(--paper);position:relative}
.backdrop{position:absolute;inset:0}
.brand-block{position:absolute;left:40px;top:240px;width:240px;text-align:center;color:var(--pink)}
.brand-mark{width:140px;height:140px;border-radius:50%;background:var(--pink);margin:0 auto 30px}
.brand-name{font-weight:900;font-size:48px;letter-spacing:2px;line-height:1}
.brand-tag{font-weight:500;font-size:16px;letter-spacing:.5px;margin-top:10px}
.phone{position:absolute;top:45px;width:263px;height:765px;background:var(--white);border-radius:22px}
.screen{position:absolute;left:9px;top:9px;width:245px;height:746px;border-radius:13px;overflow:hidden;background:var(--dark)}
.p1{left:327px}.p2{left:612px}.p3{left:897px}
.splash{background:linear-gradient(180deg,var(--coral) 0%,#ef5260 50%,var(--pink) 100%);display:flex;flex-direction:column;align-items:center;justify-content:center;color:var(--white);padding-top:10px}
.splash .mark{width:62px;height:62px;border-radius:50%;background:var(--white);margin-bottom:14px}
.splash .name{font-weight:900;font-size:22px;letter-spacing:1px;line-height:1}
.splash .tag{font-weight:500;font-size:7.5px;letter-spacing:.4px;margin-top:5px}
.map{position:absolute;left:0;top:0;width:245px;height:340px;
  background:
    radial-gradient(ellipse 60% 40% at 85% 85%,rgba(180,140,40,.28),transparent 70%),
    radial-gradient(ellipse 50% 35% at 10% 70%,rgba(180,140,40,.22),transparent 70%),
    radial-gradient(ellipse 55% 30% at 60% 15%,rgba(180,140,40,.2),transparent 70%),
    radial-gradient(ellipse 70% 50% at 45% 45%,var(--map-light),transparent 75%),
    linear-gradient(160deg,#303135 0%,var(--map) 55%,#26272b 100%)}
.radius{position:absolute;border-radius:50%;background:rgba(255,255,255,.14)}
.me{position:absolute;width:8px;height:8px;border-radius:50%;background:var(--coral);border:2px solid #fff;box-sizing:content-box}
.pin{position:absolute;width:20px;height:20px;border-radius:50%;border:2px solid #fff;background:#5a4fa0}
.searchbar{position:absolute;top:23px;left:9px;right:11px;height:24px}
.back{position:absolute;left:0;top:0;width:23px;height:24px;background:#fff;border-radius:5px;display:flex;align-items:center;justify-content:center}
.search{position:absolute;left:32px;top:0;width:161px;height:24px;border-radius:6px;background:rgba(255,255,255,.08);color:#e4e5ea;font-size:6.5px;display:flex;align-items:center;gap:8px;padding-left:16px}
.add{position:absolute;right:0;top:0;width:22px;height:24px;background:var(--pink);border-radius:5px;display:flex;align-items:center;justify-content:center}
.sheet-cats{position:absolute;left:0;width:245px;height:130px;background:var(--pink);border-radius:12px 12px 0 0}
.handle{position:absolute;left:50%;width:50px;height:2px;margin-left:-25px;border-radius:2px;background:#fff}
.sec-head{position:absolute;left:19px;right:13px;display:flex;justify-content:space-between;align-items:baseline;color:#fff}
.sec-head h3{font-size:8px;font-weight:500;letter-spacing:.2px}
.sec-head span{font-size:5.5px;font-weight:700}
.tiles{position:absolute;left:19px;display:flex;gap:6px}
.tile{width:50px;height:44px;border-radius:5px;background:#fff;display:flex;flex-direction:column;align-items:center;justify-content:center;gap:4px;font-size:5px;font-weight:500;color:var(--dark)}
.tile.active{background:var(--dark);color:#fff}
.tile svg{width:16px;height:16px}
.sheet-dark{position:absolute;left:0;top:423px;width:245px;height:340px;background:var(--dark);border-radius:12px 12px 0 0}
.item{position:absolute;left:0;width:245px;height:62px}
.item.selected{background:var(--row)}
.item .logo{position:absolute;width:50px;height:50px;border-radius:5px;border:2px solid #fff;background:#3b3f4d}
.item h4{position:absolute;font-size:8.5px;font-weight:700;color:#fff}
.item.selected h4{color:var(--dark)}
.stars{position:absolute;font-size:6px;color:var(--star);letter-spacing:.5px;white-space:nowrap}
.stars small{color:var(--muted);font-size:4.6px;letter-spacing:0;margin-left:4px}
.dist{position:absolute;font-size:5.5px;color:var(--muted);display:flex;gap:6px;align-items:center}
.scrollbar{position:absolute;right:13px;width:2px;border-radius:2px;background:#555a68}
.sheet-peek{position:absolute;left:0;top:657px;width:245px;height:60px;background:var(--pink);border-radius:12px 12px 0 0}
.nav{position:absolute;left:0;bottom:0;width:245px;height:33px;background:#fff}
.nav svg{position:absolute;top:10px;width:13px;height:13px}
.fab{position:absolute;left:93px;top:681px;width:58px;height:58px;border-radius:50%;background:var(--pink);border:4px solid #fff;box-shadow:0 0 0 3px var(--pink)}
.fab::after{content:"";position:absolute;inset:8px;border-radius:50%;border:2px solid rgba(255,255,255,.85)}
.detail .avatar{position:absolute;left:19px;top:452px;width:62px;height:62px;border-radius:50%;border:2px solid #fff;background:#3b3f4d}
.detail h2{position:absolute;left:98px;top:466px;font-size:10.5px;font-weight:700;color:#fff}
.detail .addr{position:absolute;left:98px;top:482px;font-size:6px;color:var(--muted)}
.detail .near{position:absolute;left:98px;top:495px;font-size:5.5px;color:var(--coral);display:flex;gap:5px;align-items:center}
.spec{position:absolute;left:18px;right:20px;display:flex;justify-content:space-between;align-items:center;font-size:6.5px;color:#e4e5ea;padding-bottom:10px;border-bottom:1px solid #454a58}
.spec.last{border-bottom:none}
.spec b{font-weight:400;text-align:center}
.buy{position:absolute;left:19px;top:636px;width:206px;height:33px;border-radius:4px;background:linear-gradient(90deg,#ee5f66,var(--orange));color:var(--dark);font-size:8px;font-weight:500;display:flex;align-items:center;justify-content:center}
.peek-card{position:absolute;left:23px;top:415px;width:198px;height:12px;border-radius:8px 8px 0 0;background:#f19aac}
</style>
</head>
<body>
<svg class="backdrop" width="1200" height="857" viewBox="0 0 1200 857" aria-hidden="true">
  <path d="M0 700 C 300 560 650 560 900 480 C 1030 440 1130 420 1200 410 L1200 857 L0 857Z" fill="var(--orange)"/>
  <path d="M0 790 C 260 640 620 620 880 520 C 1010 470 1120 440 1200 430 L1200 857 L0 857Z" fill="var(--pink)"/>
  <path d="M0 857 L0 800 C 300 690 600 650 900 560 C 1030 520 1130 470 1200 450 L1200 857Z" fill="var(--coral)" opacity=".55"/>
</svg>

<div class="brand-block">
  <div class="brand-mark"></div>
  <div class="brand-name">VORELA</div>
  <div class="brand-tag">THE INSTRUCTOR'S APP</div>
</div>

<!-- Splash -->
<div class="phone p1">
  <div class="screen splash">
    <div class="mark"></div>
    <div class="name">VORELA</div>
    <div class="tag">THE INSTRUCTOR'S APP</div>
  </div>
</div>

<!-- Around me: map + list -->
<div class="phone p2">
  <div class="screen">
    <div class="map" role="img" aria-label="Dark street map of the surrounding neighbourhoods with main roads highlighted in yellow"></div>
    <div class="radius" style="left:53px;top:91px;width:106px;height:106px"></div>
    <div class="radius" style="left:75px;top:113px;width:62px;height:62px"></div>
    <div class="me" style="left:100px;top:138px"></div>
    <div class="pin" style="left:187px;top:74px;background:#2b5fb4"></div>
    <div class="pin" style="left:59px;top:170px;background:#3b3f4d"></div>
    <div class="pin" style="left:156px;top:217px"></div>
    <div class="pin" style="left:87px;top:235px;background:#e8c320"></div>
    <div class="searchbar">
      <div class="back"><svg width="8" height="8" viewBox="0 0 8 8"><path d="M5.5 1 2.5 4l3 3" fill="none" stroke="#2b2f3c" stroke-width="1.3"/></svg></div>
      <div class="search"><svg width="10" height="10" viewBox="0 0 10 10"><circle cx="4.3" cy="4.3" r="3.3" fill="none" stroke="#fff" stroke-width="1"/><path d="M6.8 6.8 9 9" stroke="#fff" stroke-width="1"/></svg>Search Around Me</div>
      <div class="add"><svg width="10" height="10" viewBox="0 0 10 10"><path d="M5 1v8M1 5h8" stroke="#fff" stroke-width="1.4"/></svg></div>
    </div>

    <div class="sheet-cats" style="top:325px">
      <div class="handle" style="top:8px"></div>
      <div class="sec-head" style="top:25px"><h3>CATEGORIES</h3><span>SEE ALL</span></div>
      <div class="tiles" style="top:43px">
        <div class="tile active"><svg viewBox="0 0 16 16"><rect x="3" y="2" width="10" height="13" fill="none" stroke="#fff"/><path d="M5 5h2M9 5h2M5 8h2M9 8h2M5 11h2M9 11h2" stroke="#fff"/></svg>Facilities</div>
        <div class="tile"><svg viewBox="0 0 16 16"><circle cx="6" cy="5" r="2.5" fill="none" stroke="#e23e62"/><path d="M1.5 14c0-3 2-5 4.5-5s4.5 2 4.5 5" fill="none" stroke="#e23e62"/><circle cx="11.5" cy="6" r="2" fill="none" stroke="#e23e62"/><path d="M11 9.5c2 0 3.5 1.6 3.5 4" fill="none" stroke="#e23e62"/></svg>Professionals</div>
        <div class="tile"><svg viewBox="0 0 16 16"><path d="M1 6l7-3 7 3-7 3z" fill="#e23e62"/><path d="M4 8v3.5c2 1.5 6 1.5 8 0V8" fill="none" stroke="#e23e62"/></svg>Classes</div>
        <div class="tile"><svg viewBox="0 0 16 16"><path d="M2 6l3-3.5h6L14 6l-6 8z M2 6h12" fill="none" stroke="#e23e62"/></svg>Brands</div>
        <div class="tile"></div>
      </div>
    </div>

    <div class="sheet-dark">
      <div class="handle" style="top:10px"></div>
      <div class="sec-head" style="top:30px"><h3 style="font-size:8px">NEARBY DESTINATIONS</h3><span style="color:var(--coral)">MORE</span></div>
      <div class="scrollbar" style="top:97px;height:38px"></div>
      <div class="scrollbar" style="top:170px;height:40px"></div>

      <div class="item" style="top:56px">
        <div class="logo" style="left:19px;top:2px"></div>
        <h4 style="left:83px;top:13px">Ironhold Gym House</h4>
        <div class="stars" style="left:83px;top:26px">★★★★☆<small>Rating: 4/5 · 1,574 Votes</small></div>
        <div class="dist" style="left:84px;top:38px"><svg width="7" height="8" viewBox="0 0 7 8"><path d="M3.5 7.5S6.5 4.6 6.5 3a3 3 0 0 0-6 0c0 1.6 3 4.5 3 4.5z" fill="none" stroke="#e23e62"/><circle cx="3.5" cy="3" r="1" fill="#e23e62"/></svg>2.5 Km</div>
      </div>

      <div class="item selected" style="top:121px;height:70px">
        <div class="logo" style="left:17px;top:10px;background:#4a3a8e"></div>
        <h4 style="left:81px;top:20px">Ironhold Gym House</h4>
        <div class="stars" style="left:81px;top:33px">★★★★☆<small>Rating: 4/5 · 1,574 Votes</small></div>
        <div class="dist" style="left:82px;top:45px"><svg width="7" height="8" viewBox="0 0 7 8"><path d="M3.5 7.5S6.5 4.6 6.5 3a3 3 0 0 0-6 0c0 1.6 3 4.5 3 4.5z" fill="none" stroke="#e23e62"/><circle cx="3.5" cy="3" r="1" fill="#e23e62"/></svg>2.5 Km</div>
      </div>

      <div class="item" style="top:198px">
        <div class="logo" style="left:19px;top:2px;background:#e8c320"></div>
        <h4 style="left:83px;top:11px">Ironhold Gym House</h4>
        <div class="stars" style="left:83px;top:24px">★★★★☆<small>Rating: 4/5 · 1,574 Votes</small></div>
      </div>
    </div>

    <div class="sheet-peek"><div class="handle" style="top:9px"></div></div>
    <div class="nav">
      <svg style="left:23px" viewBox="0 0 13 13"><circle cx="6.5" cy="6.5" r="6.5" fill="#1e2029"/><path d="M3.5 6.5 9.5 4 7.5 9.8 6.6 7.3z" fill="none" stroke="#fff" stroke-width=".8"/></svg>
      <svg style="left:64px" viewBox="0 0 13 13"><circle cx="4.5" cy="4" r="2" fill="none" stroke="#b8bcc6"/><circle cx="8.8" cy="4.5" r="1.7" fill="none" stroke="#b8bcc6"/><path d="M1 12c0-2.5 1.5-4.5 3.5-4.5S8 9.5 8 12M8.5 7.5c2 0 3.5 1.6 3.5 4" fill="none" stroke="#b8bcc6"/></svg>
      <svg style="left:173px" viewBox="0 0 13 13"><rect x="1" y="3.5" width="8" height="6.5" rx="1.5" fill="none" stroke="#b8bcc6"/><path d="M9 6l3-2v5.5L9 7.5" fill="none" stroke="#b8bcc6"/></svg>
      <svg style="left:211px" viewBox="0 0 13 13"><path d="M1 3.5h11M1 6.5h11M1 9.5h7" stroke="#b8bcc6"/></svg>
    </div>
    <div class="fab"></div>
  </div>
</div>

<!-- Facility detail -->
<div class="phone p3">
  <div class="screen detail">
    <div class="map" role="img" aria-label="Dark street map of the surrounding neighbourhoods with main roads highlighted in yellow"></div>
    <div class="radius" style="left:53px;top:91px;width:106px;height:106px"></div>
    <div class="radius" style="left:75px;top:113px;width:62px;height:62px"></div>
    <div class="me" style="left:100px;top:138px"></div>
    <div class="pin" style="left:187px;top:74px;background:#2b5fb4"></div>
    <div class="pin" style="left:59px;top:170px;background:#3b3f4d"></div>
    <div class="pin" style="left:156px;top:217px"></div>
    <div class="pin" style="left:87px;top:235px;background:#e8c320"></div>
    <div class="searchbar">
      <div class="back"><svg width="8" height="8" viewBox="0 0 8 8"><path d="M5.5 1 2.5 4l3 3" fill="none" stroke="#2b2f3c" stroke-width="1.3"/></svg></div>
      <div class="search"><svg width="10" height="10" viewBox="0 0 10 10"><circle cx="4.3" cy="4.3" r="3.3" fill="none" stroke="#fff" stroke-width="1"/><path d="M6.8 6.8 9 9" stroke="#fff" stroke-width="1"/></svg>Search Around Me</div>
      <div class="add"><svg width="10" height="10" viewBox="0 0 10 10"><path d="M5 1v8M1 5h8" stroke="#fff" stroke-width="1.4"/></svg></div>
    </div>

    <div class="sheet-cats" style="top:314px">
      <div class="handle" style="top:8px"></div>
      <div class="sec-head" style="top:24px"><h3>CATEGORIES</h3><span>SEE ALL</span></div>
      <div class="tiles" style="top:43px">
        <div class="tile active"><svg viewBox="0 0 16 16"><rect x="3" y="2" width="10" height="13" fill="none" stroke="#fff"/><path d="M5 5h2M9 5h2M5 8h2M9 8h2M5 11h2M9 11h2" stroke="#fff"/></svg>Facilities</div>
        <div class="tile"><svg viewBox="0 0 16 16"><circle cx="6" cy="5" r="2.5" fill="none" stroke="#e23e62"/><path d="M1.5 14c0-3 2-5 4.5-5s4.5 2 4.5 5" fill="none" stroke="#e23e62"/><circle cx="11.5" cy="6" r="2" fill="none" stroke="#e23e62"/><path d="M11 9.5c2 0 3.5 1.6 3.5 4" fill="none" stroke="#e23e62"/></svg>Professionals</div>
        <div class="tile"><svg viewBox="0 0 16 16"><path d="M1 6l7-3 7 3-7 3z" fill="#e23e62"/><path d="M4 8v3.5c2 1.5 6 1.5 8 0V8" fill="none" stroke="#e23e62"/></svg>Classes</div>
        <div class="tile"><svg viewBox="0 0 16 16"><path d="M2 6l3-3.5h6L14 6l-6 8z M2 6h12" fill="none" stroke="#e23e62"/></svg>Brands</div>
        <div class="tile"></div>
      </div>
    </div>
    <div class="peek-card"></div>

    <div class="sheet-dark"><div class="handle" style="top:10px"></div></div>
    <div class="avatar"></div>
    <h2>Ironhold Gym House</h2>
    <div class="addr">48 Harbor Lane, Westbrook, NY 10412</div>
    <div class="near"><svg width="8" height="9" viewBox="0 0 7 8"><path d="M3.5 7.5S6.5 4.6 6.5 3a3 3 0 0 0-6 0c0 1.6 3 4.5 3 4.5z" fill="none" stroke="#f86b5a"/><circle cx="3.5" cy="3" r="1" fill="#f86b5a"/></svg>300m / 5 Min.</div>

    <div class="spec" style="top:539px"><span>The Size Of The Fitness</span><b>1000 M2</b></div>
    <div class="spec" style="top:570px"><span>The Capabilities Of The Fitness</span><b>Free Weight, Cardio,<br>Sauna</b></div>
    <div class="spec last" style="top:609px"><span>Opening Hours</span><b>10 AM - 11 PM</b></div>
    <div class="buy">Buy Access To The Fitness</div>

    <div class="nav">
      <svg style="left:23px" viewBox="0 0 13 13"><circle cx="6.5" cy="6.5" r="6.5" fill="#1e2029"/><path d="M3.5 6.5 9.5 4 7.5 9.8 6.6 7.3z" fill="none" stroke="#fff" stroke-width=".8"/></svg>
      <svg style="left:64px" viewBox="0 0 13 13"><circle cx="4.5" cy="4" r="2" fill="none" stroke="#b8bcc6"/><circle cx="8.8" cy="4.5" r="1.7" fill="none" stroke="#b8bcc6"/><path d="M1 12c0-2.5 1.5-4.5 3.5-4.5S8 9.5 8 12M8.5 7.5c2 0 3.5 1.6 3.5 4" fill="none" stroke="#b8bcc6"/></svg>
      <svg style="left:173px" viewBox="0 0 13 13"><rect x="1" y="3.5" width="8" height="6.5" rx="1.5" fill="none" stroke="#b8bcc6"/><path d="M9 6l3-2v5.5L9 7.5" fill="none" stroke="#b8bcc6"/></svg>
      <svg style="left:211px" viewBox="0 0 13 13"><path d="M1 3.5h11M1 6.5h11M1 9.5h7" stroke="#b8bcc6"/></svg>
    </div>
    <div class="fab" style="box-shadow:0 0 0 3px var(--dark)"></div>
  </div>
</div>
</body>
</html>
```